Wine Bottle Label and Logo Design

Wine label needed for small family winery, Hollow Creek Acres Cellars. Draft logo and palette created but need more work on Logo also.
Would like a simple label that has the HCA logo with space to put the wine varietal on the front.

We have a sustainably farmed vineyard, Pemberly Vineyards, which provides the estate grown fruit. We have recently been profiled in the news for our composting efforts. This links shares that and a bit of our story about Hollow Creek Acres and the western novelist Talia Brisk that our wine is named after.
https://www.examplenewsdesk.test/local/farm-mulch-story-helps-soil-health/4812290/.

Website of www.pemberlyvineyards.test also has more background (and we are working an update on this as well as need a HCAWines.test website). The back of the wine label will have the Pemberly Vineyards logo.

We are a verified micro-producer with Smallgrowerpledge.test and want this logo on the front of label.

Attached are sample labels from prior vintages, color palette, logos, and snippets about Tailа Brisk.

The HCA logo attached has reference to a blue line stream on our property and is meant to resemble a cattle brand - simple with reference to the land.

We want the label to be reminiscent of a 1920's era ranch, again with the Tailа Brisk theme (see more about her at https://archive.mapleridgeuniv.test/digital/collection/brisk/search).

Target Market(s)

Wine drinkers, sustainable agriculture

Industry/Entity Type

Wine, agriculture, sustainability

Colors

Designer to choose colors to be used in the design.

Requirements
Must have
• 1920's ranch feel, simple. Include SGP logo on front label
Nice to have
• Color palette as presented on prior Tin Lantern lable
Should not have
• Anything gilded, pompous, too busy

```html
<!DOCTYPE html>
<html lang="en">
<head>
<meta charset="utf-8">
<title>Hollow Creek Acres Cellars – Sauvignon Blanc Label</title>
<link href="https://fonts.googleapis.com/css2?family=Cinzel:wght@700&family=Kaushan+Script&display=swap" rel="stylesheet">
<style>
  :root {
    --backdrop: #e4e4e4;
    --paper: #ece9e1;
    --sage: #9dbb8c;
    --gold-dark: #8a6a2a;
    --gold-light: #e2c67a;
    --brand-gold: #9a7632;
    --ink: #23251f;
    --barn-light: #8aa57c;
    --barn-mid: #5f7658;
    --barn-dark: #3c4a38;
    --seal-dark: #3a2f28;
    --seal-rim: #b89458;
    --seal-inner: #5a4a3e;
  }
  * { margin: 0; padding: 0; box-sizing: border-box; }
  html, body {
    width: 1200px;
    height: 900px;
    overflow: hidden;
    background: var(--backdrop);
  }
  .canvas {
    position: relative;
    width: 1200px;
    height: 900px;
  }
  .label {
    position: absolute;
    left: 396px;
    top: 50px;
    width: 408px;
    height: 800px;
    background: var(--sage);
    overflow: hidden;
    box-shadow: 0 6px 24px rgba(0,0,0,0.12);
  }
  .gold-rule {
    position: absolute;
    left: 0;
    width: 100%;
    background: linear-gradient(90deg, var(--gold-dark), var(--gold-light) 45%, var(--gold-dark));
  }
  .gold-rule--top { top: 0; height: 10px; }
  .gold-rule--bottom { top: 686px; height: 30px; }
  .brand-panel {
    position: absolute;
    top: 10px;
    left: 0;
    width: 100%;
    height: 196px;
    background: var(--paper);
  }
  .brand-name {
    position: absolute;
    left: 0;
    width: 100%;
    text-align: center;
    font-family: "Cinzel", serif;
    font-weight: 700;
    color: var(--brand-gold);
    line-height: 1;
  }
  .brand-name--mark {
    top: 96px;
    font-size: 44px;
    letter-spacing: 3px;
  }
  .brand-name--sub {
    top: 146px;
    font-size: 10px;
    letter-spacing: 5px;
    padding-left: 5px;
  }
  .barn-illustration {
    position: absolute;
    top: 332px;
    left: 40px;
    width: 326px;
    height: 210px;
    background:
      radial-gradient(ellipse at 60% 55%, var(--barn-light) 0%, var(--barn-mid) 55%, transparent 78%),
      radial-gradient(ellipse at 25% 70%, var(--barn-dark) 0%, transparent 60%);
  }
  .varietal {
    position: absolute;
    top: 562px;
    left: 0;
    width: 100%;
    text-align: center;
    font-family: "Kaushan Script", cursive;
    font-weight: 400;
    font-size: 42px;
    line-height: 60px;
    color: var(--ink);
  }
  .pledge-seal {
    position: absolute;
    top: 678px;
    left: 154px;
  }
</style>
</head>
<body>
  <main class="canvas">
    <article class="label" aria-label="Hollow Creek Acres Cellars Sauvignon Blanc front label">
      <div class="gold-rule gold-rule--top"></div>
      <header class="brand-panel">
        <span class="brand-name brand-name--mark">HCA</span>
        <span class="brand-name brand-name--sub">WINES</span>
      </header>
      <div class="barn-illustration" role="img" aria-label="Engraved illustration of a 1920s ranch barn with a figure by the door"></div>
      <h1 class="varietal">Sauvignon Blanc</h1>
      <div class="gold-rule gold-rule--bottom"></div>
      <svg class="pledge-seal" width="100" height="100" viewBox="0 0 100 100" role="img" aria-label="Small grower pledge verified micro-producer seal">
        <circle cx="50" cy="50" r="48" fill="var(--seal-dark)" stroke="var(--seal-rim)" stroke-width="3"/>
        <circle cx="50" cy="50" r="32" fill="var(--seal-inner)" stroke="var(--seal-rim)" stroke-width="1.5"/>
      </svg>
    </article>
  </main>
</body>
</html>
```